Business Cards and stationary for personal wealth management company
Stoneharbor Capital
Creative Brief
Simple
Martin J Hollis, CRPC®
President | Wealth Management
4471 SW Alder Ave Ste 115 Bellevue, WA 98007
martin.hollis@qvm-example.com
www.stoneharborcapital-example.com
>> I need a 2 sided business card and supporting stationary. disclosure: I am thinking of using the disclosure language noted below - at the bottom of the backside of the business card. Securities offered through QVM Securities, member NASTRO/CIRF Also - On the back of the business card - I would like to consider a watermarked image on a darker background with the text in a lighter font. Also - I want to consider a tagline on the front: not sure I will use a tagline though. Tagline idea: Putting Your Wealth to Work for You! (or) Our Independence - Your Advantage!
Our Mission Our purpose is to deliver exceptional financial guidance and personalized service to help you build and preserve your wealth, create a strategy for passing on a lasting heritage to loved ones or meaningful charities, and empower you to pursue your life’s aspirations. Our Independence - Your Advantage! Stoneharbor is uniquely positioned to cater to your distinct financial needs. As your trusted financial advocate, we provide unbiased investment guidance and financial planning to help you manage your wealth over your lifetime and beyond. We have no proprietary investment products to sell and no investment banking relationships to promote. Putting Your Wealth to Work for You! We start by gaining a deep understanding of your values, goals and unique perspectives. Once we have insight into your distinct financial situation, we begin to design a highly customized, integrated wealth management solution.

```html
<!DOCTYPE html>
<html lang="en">
<head>
<meta charset="utf-8">
<title>Stoneharbor Capital – Business Card</title>
<link rel="stylesheet" href="https://fonts.googleapis.com/css2?family=Michroma&family=Open+Sans:wght@400;600&display=swap">
<style>
  :root {
    --navy: #3b3f73;
    --navy-deep: #2f3363;
    --silver-light: #f4f4f5;
    --silver-dark: #c9cacd;
    --swoosh: #9a9ca3;
    --paper: #ffffff;
    --stage: #e9e7e3;
    --ink-light: #ffffff;
    --ink-muted: #d9dbe8;
  }
  * { box-sizing: border-box; margin: 0; padding: 0; }
  html, body {
    width: 1200px; height: 899px; overflow: hidden;
    background: var(--stage);
    font-family: "Open Sans", Arial, sans-serif;
  }
  .canvas { position: relative; width: 1200px; height: 899px; }

  .card {
    position: absolute;
    width: 630px; height: 360px;
    border-radius: 4px;
    overflow: hidden;
    box-shadow: 0 10px 28px rgba(0,0,0,0.18);
  }

  /* back side */
  .card-back { left: 500px; top: 60px; background: var(--paper); }
  .card-back .brand {
    position: absolute; left: 0; right: 0; top: 138px;
    text-align: center; color: var(--navy);
    font-family: "Michroma", Arial, sans-serif;
  }
  .brand-name { font-size: 38px; letter-spacing: 1px; line-height: 1; }
  .brand-sub { font-size: 13px; letter-spacing: 9px; margin-top: 8px; }

  /* front side */
  .card-front { left: 90px; top: 470px; background: var(--silver-light); }
  .card-front .bands { position: absolute; inset: 0; }
  .card-front .brand {
    position: absolute; left: 28px; top: 36px;
    color: var(--navy);
    font-family: "Michroma", Arial, sans-serif;
  }
  .card-front .brand-name { font-size: 33px; }
  .card-front .brand-sub { font-size: 11px; letter-spacing: 8px; margin-top: 6px; padding-left: 40px; }

  .person {
    position: absolute; right: 30px; top: 118px; text-align: right;
  }
  .person-name {
    font-family: "Michroma", Arial, sans-serif;
    font-size: 16px; color: var(--navy); letter-spacing: 0.5px;
  }
  .person-title { font-size: 13px; color: var(--navy-deep); margin-top: 4px; font-weight: 600; }

  .contact-list {
    position: absolute; left: 26px; top: 178px; list-style: none;
    color: var(--ink-light); font-size: 11.5px;
  }
  .contact-list li { display: flex; align-items: center; gap: 9px; height: 23px; }
  .contact-list svg { width: 12px; height: 12px; fill: var(--ink-muted); }

  .address {
    position: absolute; right: 30px; top: 226px; text-align: right;
    color: var(--ink-light); font-size: 12px; line-height: 1.45;
  }
  .website {
    position: absolute; right: 30px; bottom: 24px;
    color: var(--ink-light); font-size: 12.5px; letter-spacing: 0.3px;
  }
</style>
</head>
<body>
<main class="canvas">

  <section class="card card-back" aria-label="Business card back">
    <div class="brand">
      <div class="brand-name">STONEHARBOR</div>
      <div class="brand-sub">CAPITAL</div>
    </div>
  </section>

  <section class="card card-front" aria-label="Business card front">
    <svg class="bands" viewBox="0 0 630 360" preserveAspectRatio="none" aria-hidden="true">
      <defs>
        <linearGradient id="silver" x1="0" y1="0" x2="1" y2="1">
          <stop offset="0" stop-color="#fafafa"/>
          <stop offset="1" stop-color="#cfd0d3"/>
        </linearGradient>
      </defs>
      <rect width="630" height="360" fill="url(#silver)"/>
      <path d="M0 150 C 200 132, 420 158, 630 205 L630 360 L0 360 Z" fill="var(--navy)"/>
      <path d="M0 144 C 200 124, 420 150, 630 196" fill="none" stroke="var(--swoosh)" stroke-width="4"/>
    </svg>

    <div class="brand">
      <div class="brand-name">STONEHARBOR</div>
      <div class="brand-sub">CAPITAL</div>
    </div>

    <div class="person">
      <div class="person-name">PETER LANGFORD</div>
      <div class="person-title">Managing Director</div>
    </div>

    <ul class="contact-list">
      <li><svg viewBox="0 0 12 12"><path d="M2.5 0.5 L4.5 0.5 L5.2 3 L4 4.2 C4.6 5.6 6.4 7.4 7.8 8 L9 6.8 L11.5 7.5 L11.5 9.5 C11.5 10.6 10.6 11.5 9.5 11.5 C4.5 11.5 0.5 7.5 0.5 2.5 C0.5 1.4 1.4 0.5 2.5 0.5 Z"/></svg>014 555 0192</li>
      <li><svg viewBox="0 0 12 12"><rect x="3" y="0.5" width="6" height="11" rx="1"/><rect x="4" y="1.8" width="4" height="7" fill="var(--navy)"/></svg>014 555 0192</li>
      <li><svg viewBox="0 0 12 12"><rect x="2" y="0.5" width="8" height="4"/><rect x="0.5" y="4" width="11" height="5" rx="1"/><rect x="2.5" y="7.5" width="7" height="4"/></svg>014 555 0192</li>
      <li><svg viewBox="0 0 12 12"><rect x="0.5" y="2" width="11" height="8" rx="1"/><path d="M1 2.5 L6 6.5 L11 2.5" stroke="var(--navy)" stroke-width="1.2" fill="none"/></svg>yourname@mail-example.com</li>
    </ul>

    <address class="address">071 12th Floor Quay<br>Harbour Road LAG</address>
    <div class="website">www.yoursite-example.com</div>
  </section>

</main>
</body>
</html>
```